PPE EQIUPMENT

WE WOULD LIKE TO PRODUCE 2 DIFFERENT BANNERS TO BE PLACED OUTSIDE OF OUR WAREHOUSE TO ADVERTISE THAT WE HAVE FACE MASKS, HAND SANITISERS, DISINFECTANT SPRAY, FACE SHIELDS AND HAND SOAP. THE SIZE OF EACH BANNER WILL BE , portrait to be (W) 140 cm x (H) 250 cm, with 4 x eyelets. THE BANNER IS TO STATE PPE EQUIPMENT AVAILABLE HERE AND SHOW OUR PHONE NUMBER 0207-946-0318. FINALLY WE WILL REQUIRE SOME IMAGES OF THE PRODUCTS IF YOU CAN SUPPLY THESE. THANKS

```html
<!DOCTYPE html>
<html lang="en">
<head>
<meta charset="utf-8">
<title>PPE Equipment Banner – Holtby Interiors</title>
<link rel="stylesheet" href="https://fonts.googleapis.com/css2?family=Barlow:wght@300;500&family=Barlow+Condensed:wght@700&family=Heebo:wght@700;800&display=swap">
<style>
  :root{
    --navy:#213a70;
    --ink:#0b0b0b;
    --paper:#ffffff;
    --paper-shade:#e9eaec;
    --footer:#333333;
    --sky:#5cc4ef;
    --sky-deep:#2a8fd0;
    --teal:#1b6f9a;
    --backdrop:#5b5b5b;
  }
  *{margin:0;padding:0;box-sizing:border-box}
  html,body{width:840px;height:1200px;overflow:hidden}
  body{background:var(--backdrop);position:relative}
  .banner{position:absolute;left:95px;top:20px;width:650px;height:1160px}
  .banner svg{display:block;width:100%;height:100%}
  .brand-name{font-family:"Barlow",sans-serif;font-weight:500;font-size:84px;fill:var(--paper)}
  .brand-tagline{font-family:"Barlow",sans-serif;font-weight:300;font-size:44px;letter-spacing:2px;fill:var(--paper)}
  .product-label{font-family:"Heebo",sans-serif;font-weight:700;font-size:44px;fill:var(--paper)}
  .headline{font-family:"Heebo",sans-serif;font-weight:800;font-size:96px;fill:var(--ink)}
  .headline-sub{font-family:"Heebo",sans-serif;font-weight:800;font-size:74px;fill:var(--paper)}
  .item-name{font-family:"Heebo",sans-serif;font-weight:700;font-size:40px;fill:var(--ink)}
  .phone-number{font-family:"Barlow Condensed",sans-serif;font-weight:700;font-size:118px;fill:var(--paper)}
  .web-address{font-family:"Barlow",sans-serif;font-weight:500;font-size:46px;fill:var(--paper)}
  .rule{stroke:var(--navy);stroke-width:2}
  .label-plate{fill:var(--navy)}
</style>
</head>
<body>
<div class="banner">
<svg viewBox="0 0 913 1630" xmlns="http://www.w3.org/2000/svg">
  <defs>
    <linearGradient id="body-wash" x1="0" y1="0" x2="1" y2="1">
      <stop offset="0" stop-color="var(--paper)"/>
      <stop offset="0.55" stop-color="#f4f4f5"/>
      <stop offset="1" stop-color="var(--paper-shade)"/>
    </linearGradient>
    <linearGradient id="product-blue" x1="0" y1="0" x2="0" y2="1">
      <stop offset="0" stop-color="#8fdcf7"/>
      <stop offset="1" stop-color="var(--sky-deep)"/>
    </linearGradient>
    <linearGradient id="shield-clear" x1="0" y1="0" x2="0" y2="1">
      <stop offset="0" stop-color="#f2f4f6"/>
      <stop offset="1" stop-color="#dfe3e8"/>
    </linearGradient>
    <linearGradient id="teal-disc" x1="0" y1="0" x2="0" y2="1">
      <stop offset="0" stop-color="#2f8cbc"/>
      <stop offset="1" stop-color="var(--teal)"/>
    </linearGradient>
  </defs>

  <rect class="banner-body" x="0" y="0" width="913" height="1630" fill="url(#body-wash)"/>

  <g class="banner-header">
    <rect x="0" y="0" width="913" height="237" fill="var(--navy)"/>
    <text class="brand-name" x="456" y="128" text-anchor="middle" textLength="700" lengthAdjust="spacingAndGlyphs">HOLTBY INTERIORS</text>
    <text class="brand-tagline" x="456" y="183" text-anchor="middle" textLength="610" lengthAdjust="spacingAndGlyphs">TRADE FURNITURE SOLUTIONS</text>
  </g>

  <g class="product-row face-masks">
    <rect role="img" aria-label="Illustration of respirator and surgical face masks" x="80" y="275" width="262" height="145" rx="60" fill="url(#product-blue)" opacity="0.85"/>
    <line class="rule" x1="342" y1="312" x2="830" y2="312"/>
    <line class="rule" x1="342" y1="387" x2="830" y2="387"/>
    <polygon class="label-plate" points="386,301 746,301 780,401 418,401"/>
    <text class="product-label" x="583" y="368" text-anchor="middle">FACE MASKS</text>
  </g>

  <g class="product-row hand-sanitisers">
    <line class="rule" x1="84" y1="533" x2="640" y2="533"/>
    <line class="rule" x1="84" y1="608" x2="640" y2="608"/>
    <polygon class="label-plate" points="140,521 596,521 633,623 173,623"/>
    <text class="product-label" x="386" y="588" text-anchor="middle">HAND SANITISERS</text>
    <rect role="img" aria-label="Illustration of a hand sanitiser pump bottle" x="640" y="425" width="185" height="225" rx="40" fill="url(#product-blue)" opacity="0.85"/>
  </g>

  <g class="headline-block">
    <text class="headline" x="455" y="777" text-anchor="middle" textLength="700" lengthAdjust="spacingAndGlyphs">PPE EQUIPMENT</text>
    <rect x="105" y="803" width="703" height="99" fill="var(--navy)"/>
    <text class="headline-sub" x="456" y="877" text-anchor="middle" textLength="590" lengthAdjust="spacingAndGlyphs">AVAILABLE HERE</text>
  </g>

  <g class="product-row face-shields">
    <rect role="img" aria-label="Illustration of two clear face shields with blue headbands" x="78" y="960" width="290" height="150" rx="30" fill="url(#shield-clear)"/>
    <line class="rule" x1="370" y1="992" x2="831" y2="992"/>
    <line class="rule" x1="370" y1="1066" x2="831" y2="1066"/>
    <polygon class="label-plate" points="420,980 780,980 815,1081 454,1081"/>
    <text class="product-label" x="616" y="1047" text-anchor="middle">FACE SHIELDS</text>
  </g>

  <g class="product-pair">
    <circle role="img" aria-label="Illustration of a bar of hand soap with bubbles" cx="165" cy="1222" r="77" fill="url(#teal-disc)"/>
    <text class="item-name" x="260" y="1217">HAND</text>
    <text class="item-name" x="260" y="1262">SOAP</text>

    <circle role="img" aria-label="Illustration of a disinfectant spray bottle" cx="491" cy="1222" r="77" fill="url(#teal-disc)"/>
    <text class="item-name" x="578" y="1212">DISINFECTANT</text>
    <text class="item-name" x="578" y="1258">SPRAY</text>
  </g>

  <g class="banner-footer">
    <rect x="0" y="1427" width="913" height="203" fill="var(--footer)"/>
    <rect x="56" y="1351" width="800" height="136" rx="68" fill="var(--navy)" stroke="var(--paper)" stroke-width="3"/>
    <text class="phone-number" x="456" y="1460" text-anchor="middle" textLength="655" lengthAdjust="spacingAndGlyphs">0207-946-0318</text>
    <g class="phone-icon">
      <circle cx="89" cy="1355" r="34" fill="#2b2b2b" stroke="var(--paper)" stroke-width="3"/>
      <path transform="translate(68 1334) scale(1.75)" fill="var(--paper)" d="M6.6 10.8c1.4 2.8 3.8 5.1 6.6 6.6l2.2-2.2c.3-.3.7-.4 1-.2 1.1.4 2.3.6 3.6.6.6 0 1 .4 1 1V20c0 .6-.4 1-1 1C10.6 21 3 13.4 3 4c0-.6.4-1 1-1h3.5c.6 0 1 .4 1 1 0 1.3.2 2.5.6 3.6.1.3 0 .7-.2 1z"/>
    </g>
    <text class="web-address" x="456" y="1553" text-anchor="middle" textLength="440" lengthAdjust="spacing">www.holtby.example</text>
  </g>
</svg>
</div>
</body>
</html>
```